I need a label design/logo for a Shea Body Butter that I making. The body butter is made using Unrefined Shea Butter from Uganda. I have different mixes for the body butter depending on the Essential Oil used, for example - sweet orange, lavender, rosemary. The species of Shea tree in Uganda (Vitellaria Nilotica) is different from the one in West Africa (Vitellaria Paradoxa). As such, I would like the logo/label to have some reference to the Shea nut tree as well as the River Nile. Colours should be "fresh and earthy". I will be using round containers and I would like to be able to place the logo/label on round templates that I can stick on the containers. The name of the brand is "Teka Rumi" Shea Body Butter.

```html
<!DOCTYPE html>
<html lang="en">
<head>
<meta charset="utf-8">
<title>Teka Rumi Shea Body Butter – Round Label</title>
<link rel="stylesheet" href="https://fonts.googleapis.com/css2?family=Didact+Gothic&family=Libre+Caslon+Text:wght@400&family=Open+Sans:wght@400&display=swap">
<style>
  :root {
    --page-bg: #f7f5f3;
    --label-brown: #5a4b44;
    --pattern-brown: #54453e;
    --ring-orange: #d4561b;
    --ink-white: #fbfaf8;
    --ink-silver: #cbc6c2;
    --ribbon-dark: #7a4a16;
    --ribbon-mid: #a8701f;
    --ribbon-light: #c48c33;
    --ribbon-text: #e4651c;
  }
  html, body {
    margin: 0;
    padding: 0;
    width: 1200px;
    height: 1131px;
    overflow: hidden;
    background: var(--page-bg);
  }
  .label-canvas {
    display: block;
    width: 1200px;
    height: 1131px;
  }
  .brand-name {
    font-family: "Didact Gothic", sans-serif;
    font-size: 54px;
    fill: var(--ink-silver);
    letter-spacing: 2px;
  }
  .product-line {
    font-family: "Libre Caslon Text", serif;
    font-size: 84px;
    fill: var(--ink-white);
    letter-spacing: 34px;
  }
  .product-name {
    font-family: "Libre Caslon Text", serif;
    font-size: 100px;
    fill: var(--ink-white);
  }
  .scent-name {
    font-family: "Open Sans", sans-serif;
    font-size: 52px;
    fill: var(--ribbon-text);
  }
</style>
</head>
<body>
<svg class="label-canvas" viewBox="0 0 1200 1131" xmlns="http://www.w3.org/2000/svg">
  <defs>
    <linearGradient id="ribbon-face" x1="0" y1="0" x2="1" y2="0">
      <stop offset="0" stop-color="var(--ribbon-dark)"/>
      <stop offset="0.5" stop-color="var(--ribbon-light)"/>
      <stop offset="1" stop-color="var(--ribbon-mid)"/>
    </linearGradient>
  </defs>

  <g class="round-label">
    <circle class="label-base" cx="600" cy="565" r="485" fill="var(--label-brown)"/>
    <circle class="label-pattern" cx="600" cy="565" r="455" fill="var(--pattern-brown)"
            role="img" aria-label="Subtle tone-on-tone floral mandala pattern"/>
    <circle class="label-ring" cx="600" cy="565" r="462" fill="none"
            stroke="var(--ring-orange)" stroke-width="8"/>

    <g class="brand-mark">
      <circle class="brand-dot" cx="600" cy="330" r="62" fill="none"
              stroke="var(--ink-silver)" stroke-width="4"/>
      <text class="brand-name" x="600" y="452" text-anchor="middle">TEKA RUMI</text>
    </g>

    <text class="product-line" x="617" y="585" text-anchor="middle">SHEA</text>
    <text class="product-name" x="600" y="700" text-anchor="middle"
          textLength="706" lengthAdjust="spacingAndGlyphs">BODY BUTTER</text>

    <g class="scent-ribbon">
      <rect class="ribbon-tail" x="255" y="778" width="110" height="78" fill="var(--ribbon-dark)"/>
      <rect class="ribbon-tail" x="835" y="778" width="110" height="78" fill="var(--ribbon-dark)"/>
      <rect class="ribbon-face" x="300" y="758" width="600" height="84" fill="url(#ribbon-face)"/>
      <line x1="300" y1="761" x2="900" y2="761" stroke="var(--ring-orange)" stroke-width="3"/>
      <line x1="300" y1="839" x2="900" y2="839" stroke="var(--ring-orange)" stroke-width="3"/>
      <text class="scent-name" x="600" y="818" text-anchor="middle"
            textLength="420" lengthAdjust="spacingAndGlyphs">SWEET ORANGE</text>
    </g>
  </g>
</svg>
</body>
</html>
```